Redesign retirement planner website

Provide an original design for a website. The site should introduce the retirement planner, explain the basic offerings of his services, and invite the website visitor to enter their name, phone, and email. Please provide a ready-to-publish redesign that can actually be published via a Wordpress template or other major website builder like SquareSpace or Wix. Some introductory content is attached, but feel free to add additional sections/images/blocks/copywriting and rearrange/delete sections entirely to make your design original and compelling. Feel free to pull copywriting from here but again, do not use this original design, feel free to create an entirely NEW design and layout. tern-melon-zobr (dot) sitelarkhost (dot) com password: 1234 -- FINAL NOTE: Do not choose a stock photo of a man for the retirement planner. This website needs to work well with no photo of the retirement planner himself. Think of a non-face-focused design to win this competition.

Industry/Entity Type

Retirement planner personal website

Number of Pages Required

1 page

Font styles to use
Sans Serif
Decorative

Requirements
Must have
• Please provide a ready-to-publish redesign that can actually be published via a Wordpress template or other major website builder.

```html
<!DOCTYPE html>
<html lang="en">
<head>
<meta charset="utf-8">
<title>Dorian Whitcombe — Counselor &amp; Retirement Specialist</title>
<link rel="stylesheet" href="https://fonts.googleapis.com/css2?family=Josefin+Sans:wght@400;600;700&family=Roboto:wght@400;500;700&display=swap">
<style>
:root{
  --navy:#14185c;
  --navy-deep:#0f1248;
  --blue:#0c47a8;
  --blue-dark:#0a2f82;
  --ink:#1d1f3a;
  --muted:#55586a;
  --pale:#eef2f9;
  --line:#c9cde0;
  --white:#ffffff;
  --star:#f2b01e;
}
*{box-sizing:border-box;margin:0;padding:0}
html,body{width:1200px;height:3528px;overflow:hidden}
body{font-family:"Roboto",Arial,sans-serif;color:var(--ink);background:var(--white);position:relative}
.abs{position:absolute}

/* header */
.site-header{position:absolute;top:0;left:0;width:1200px;height:58px;background:var(--white);display:flex;align-items:center;padding:0 64px 0 112px;z-index:2}
.brand{font-family:"Josefin Sans",sans-serif;font-weight:700;font-size:30px;color:var(--navy);letter-spacing:1px;white-space:nowrap}
.nav{margin-left:auto;display:flex;align-items:center;gap:34px;font-size:15px;font-weight:500;color:var(--navy)}
.nav .active{border-bottom:2px solid var(--navy);padding-bottom:2px}
.btn{display:inline-block;background:var(--navy);color:var(--white);font-weight:700;font-size:14px;border-radius:22px;padding:12px 24px;letter-spacing:.5px;white-space:nowrap}

/* hero */
.hero{position:absolute;top:58px;left:0;width:1200px;height:542px;background:linear-gradient(120deg,#8e8b86,#c9c2b8 45%,#7b7f86)}
.hero-shade{position:absolute;inset:0;background:rgba(10,14,40,.42)}
.hero-box{position:absolute;left:320px;top:122px;width:560px;height:210px;border:2px solid rgba(255,255,255,.85);text-align:center;color:var(--white)}
.hero-name{position:absolute;left:50%;top:-26px;transform:translateX(-50%);height:50px;padding:0 26px;background:var(--white);color:var(--navy);font-family:"Josefin Sans",sans-serif;font-weight:700;font-size:28px;line-height:54px;letter-spacing:1px;white-space:nowrap}
.hero-title{margin-top:50px;font-family:"Josefin Sans",sans-serif;font-weight:700;font-size:44px;line-height:50px;letter-spacing:1px;white-space:nowrap}
.hero-sub{margin-top:10px;font-size:13px;font-weight:700;letter-spacing:.5px;white-space:nowrap}
.hero .btn{position:absolute;left:50%;transform:translateX(-50%);top:376px;background:var(--navy-deep);font-size:13px;padding:10px 22px}
.dots{position:absolute;left:575px;top:508px;display:flex;gap:8px}
.dots i{width:9px;height:9px;border-radius:50%;background:rgba(255,255,255,.55)}
.dots i.on{background:var(--white)}

/* about */
.about{position:absolute;top:600px;left:0;width:1200px;height:600px;background:var(--white)}
.about-ring{position:absolute;left:100px;top:60px;width:340px;height:340px;border-radius:50%;border:3px solid var(--line)}
.about-photo{position:absolute;left:112px;top:72px;width:316px;height:316px;border-radius:50%;background:linear-gradient(135deg,#b8b5ad,#e4e1da 50%,#8a8f94)}
.about-inset{position:absolute;left:345px;top:245px;width:160px;height:160px;border-radius:50%;border:5px solid var(--white);background:linear-gradient(135deg,#7d8a95,#c7ccd1)}
.eyebrow{font-size:11px;color:var(--muted);letter-spacing:1.5px;text-transform:uppercase}
.section-title{font-family:"Josefin Sans",sans-serif;font-weight:700;font-size:38px;color:var(--navy);letter-spacing:1px;line-height:1;white-space:nowrap}
.title-rule{display:block;width:26px;height:3px;background:var(--navy);margin-top:8px}
.about-text{position:absolute;left:640px;top:98px;width:480px}
.about-text .section-title{margin-top:6px}
.body-copy{font-size:13.5px;line-height:21px;color:var(--ink)}
.about-text .body-copy{margin-top:26px}
.about-text .btn{margin-top:24px;font-size:13px;padding:11px 22px}

/* specialties */
.specialties{position:absolute;top:1200px;left:0;width:1200px;height:620px;background:linear-gradient(180deg,var(--blue-dark),var(--blue) 60%,#1150b8)}
.spec-head{position:absolute;top:64px;width:1200px;text-align:center;color:var(--white)}
.spec-head .eyebrow{color:#c9d6f3}
.spec-head .section-title{color:var(--white);margin-top:6px}
.spec-head .title-rule{background:var(--white);margin:8px auto 0}
.card{position:absolute;top:120px;width:300px;height:428px;background:var(--white);border-radius:6px;overflow:hidden}
.card-photo{height:212px}
.card-icon{position:absolute;right:18px;top:176px;width:70px;height:70px;background:var(--white);border-radius:6px;box-shadow:0 2px 8px rgba(0,0,0,.15);display:flex;align-items:center;justify-content:center}
.card-title{margin:52px 18px 0;font-family:"Josefin Sans",sans-serif;font-weight:700;font-size:19px;color:var(--navy);letter-spacing:.5px}
.card-title::after{content:"";display:block;width:28px;height:3px;background:var(--navy);margin-top:6px}
.card .body-copy{margin:12px 18px 0;font-size:13px;line-height:19px;color:var(--muted)}
.read-more{display:inline-block;margin:22px 18px 0;font-size:13px;font-weight:700;color:var(--navy);border-bottom:1px solid var(--navy)}
.arrow{position:absolute;top:312px;width:36px;height:36px;border-radius:50%;background:var(--white);display:flex;align-items:center;justify-content:center}

/* testimonials */
.testimonials{position:absolute;top:1820px;left:0;width:1200px;height:840px;background:var(--white)}
.test-photo{position:absolute;left:610px;top:0;width:590px;height:460px;background:linear-gradient(160deg,#c7c1b6,#9fa7ad 50%,#d8d4cd);clip-path:polygon(14% 0,100% 0,100% 100%,0 100%,0 40%)}
.test-head{position:absolute;left:112px;top:88px}
.test-head .section-title{margin-top:6px}
.test-intro{position:absolute;left:112px;top:176px;width:480px}
.t-card{position:absolute;top:448px;width:364px;height:256px;background:var(--pale);text-align:center;padding:24px 22px 0}
.t-card.feature{background:var(--navy);color:var(--white)}
.t-name{font-family:"Josefin Sans",sans-serif;font-weight:700;font-size:22px;letter-spacing:.5px;color:var(--navy)}
.t-card.feature .t-name{color:var(--white)}
.stars{margin-top:6px;display:flex;justify-content:center}
.t-card .body-copy{margin-top:12px;font-size:13px;line-height:19px}
.t-card.feature .body-copy{color:var(--white)}
.avatar{position:absolute;width:64px;height:64px;border-radius:50%;border:4px solid var(--white);background:linear-gradient(135deg,#8b7a6c,#c3ab95)}
.pager{position:absolute;left:40px;width:30px;height:30px;border-radius:50%;display:flex;align-items:center;justify-content:center}

/* contact */
.contact{position:absolute;top:2660px;left:0;width:1200px;height:460px;background:var(--pale)}
.contact-head{position:absolute;left:112px;top:64px}
.contact-head .section-title{margin-top:6px}
.field{position:absolute;height:50px;background:var(--white);border:1px solid var(--line);font-size:13px;color:var(--muted);padding:16px 12px}
.field.message{height:90px}
.contact .btn{position:absolute;left:112px;top:390px;font-size:12px;padding:10px 16px;border-radius:20px}
.contact-ring{position:absolute;left:640px;top:36px;width:440px;height:440px;border-radius:50%;border:3px solid var(--line)}
.contact-photo{position:absolute;left:654px;top:50px;width:412px;height:412px;border-radius:50%;background:linear-gradient(135deg,#a88b6e,#e7d7c4 50%,#8f7b69)}

/* footer */
.site-footer{position:absolute;top:3120px;left:0;width:1200px;height:408px;background:var(--navy);color:var(--white)}
.f-brand{position:absolute;left:112px;top:76px;font-family:"Josefin Sans",sans-serif;font-weight:700;font-size:32px;letter-spacing:1px;white-space:nowrap}
.f-about{position:absolute;left:112px;top:126px;width:300px;font-size:13px;line-height:19px;color:#dfe2f3}
.f-col{position:absolute;top:72px}
.f-col h4{font-family:"Josefin Sans",sans-serif;font-weight:700;font-size:17px;letter-spacing:.5px}
.f-col h4::after{content:"";display:block;width:24px;height:2px;background:var(--white);margin-top:6px}
.f-links{list-style:none;margin-top:20px;font-size:13px;line-height:38px}
.contact-row{display:flex;gap:12px;margin-top:20px;font-size:13px;line-height:18px}
.c-icon{flex:none;width:34px;height:34px;border-radius:50%;background:var(--white);display:flex;align-items:center;justify-content:center}
.copyright{position:absolute;left:0;bottom:0;width:1200px;height:64px;border-top:1px solid rgba(255,255,255,.2);text-align:center;line-height:64px;font-size:13px}
</style>
</head>
<body>

<header class="site-header">
  <div class="brand">DORIAN WHITCOMBE</div>
  <nav class="nav">
    <span class="active">HOME</span><span>ABOUT US</span><span>SPECIALTIES</span><span>TESTIMONIALS</span>
    <span class="btn">CONTACT US</span>
  </nav>
</header>

<section class="hero">
  <div class="abs" style="inset:0" role="img" aria-label="Photo of a retired couple reviewing plans with an advisor"></div>
  <div class="hero-shade"></div>
  <div class="hero-box">
    <div class="hero-name">DORIAN WHITCOMBE</div>
    <div class="hero-title">COUNSELOR &amp;<br>RETIREMENT SPECIALIST</div>
    <div class="hero-sub">WITH A UNIQUE APPROACH TO FINANCIAL PLANNING</div>
  </div>
  <span class="btn">GET STARTED</span>
  <div class="dots"><i class="on"></i><i></i><i></i></div>
</section>

<section class="about">
  <div class="about-ring"></div>
  <div class="about-photo" role="img" aria-label="Photo of a smiling senior couple at home"></div>
  <div class="about-inset" role="img" aria-label="Photo of an older couple looking at a tablet"></div>
  <div class="about-text">
    <div class="eyebrow">Who we are</div>
    <h2 class="section-title">ABOUT US</h2>
    <span class="title-rule"></span>
    <p class="body-copy">Lorem ipsum dolor sit amet, consectetur adipiscing elit, sed do eiusmod tempor incididunt ut labore et dolore magna aliqua. Quis sem dolor ultrices gravida. Risus commodo viverra maecenas accumsan lacus vel facilisis. Lorem ipsum dolor sit amet, conse adipiscing elit, sed do eiusmod temporent ut labore et dolore magna aliqua. Quis ipsum suspendisse ultrices gravida. Risus commodo viverra maecenas accumsan lacus vel facilisis et dol temporait ut labore et dolore magna ua.</p>
    <span class="btn">READ MORE</span>
  </div>
</section>

<section class="specialties">
  <div class="spec-head">
    <div class="eyebrow">What we do</div>
    <h2 class="section-title">MY SPECIALTIES</h2>
    <span class="title-rule"></span>
  </div>

  <div class="arrow" style="left:40px"><svg width="14" height="14" viewBox="0 0 14 14"><path d="M9 2 4 7l5 5" fill="none" stroke="#14185c" stroke-width="2.4"/></svg></div>
  <div class="arrow" style="left:1124px"><svg width="14" height="14" viewBox="0 0 14 14"><path d="M5 2l5 5-5 5" fill="none" stroke="#14185c" stroke-width="2.4"/></svg></div>

  <article class="card" style="left:112px">
    <div class="card-photo" role="img" aria-label="Photo of a grandmother with her family" style="background:linear-gradient(135deg,#c9b8a5,#efe4d6)"></div>
    <div class="card-icon"><svg width="40" height="40" viewBox="0 0 40 40" fill="none" stroke="#14185c" stroke-width="2.4"><rect x="8" y="5" width="24" height="30" rx="2"/><path d="M13 13h14M13 19h14M13 25h9"/></svg></div>
    <h3 class="card-title">ESTATE PLANNING</h3>
    <p class="body-copy">Ensure your legacy is protected with comprehensive estate planning.</p>
    <span class="read-more">READ MORE</span>
  </article>

  <article class="card" style="left:452px">
    <div class="card-photo" role="img" aria-label="Photo of an advisor meeting a client couple" style="background:linear-gradient(135deg,#b7c0c8,#e6e9ec)"></div>
    <div class="card-icon"><svg width="40" height="40" viewBox="0 0 40 40" fill="none" stroke="#14185c" stroke-width="2.4"><path d="M20 5 8 10v9c0 8 5 13 12 16 7-3 12-8 12-16v-9z"/><path d="M14 20l4 4 8-8"/></svg></div>
    <h3 class="card-title">LIFE INSURANCE</h3>
    <p class="body-copy">Safeguard your family's future with tailored life insurance solutions.</p>
    <span class="read-more">READ MORE</span>
  </article>

  <article class="card" style="left:792px">
    <div class="card-photo" role="img" aria-label="Photo of a senior couple reviewing documents" style="background:linear-gradient(135deg,#a9a094,#ddd6cc)"></div>
    <div class="card-icon"><svg width="40" height="40" viewBox="0 0 40 40" fill="none" stroke="#14185c" stroke-width="2.4"><circle cx="20" cy="20" r="13"/><path d="M24 14h-6a3 3 0 0 0 0 6h4a3 3 0 0 1 0 6h-6M20 10v4M20 26v4"/></svg></div>
    <h3 class="card-title">FINAL EXPENSE</h3>
    <p class="body-copy">Prepare for life's final expenses with peace of mind. My services help.</p>
    <span class="read-more">READ MORE</span>
  </article>
</section>

<section class="testimonials">
  <div class="test-photo" role="img" aria-label="Photo of a senior couple meeting a financial counselor"></div>
  <div class="test-head">
    <div class="eyebrow">Client reviews</div>
    <h2 class="section-title">CLIENT TESTIMONIALS</h2>
    <span class="title-rule"></span>
  </div>
  <p class="test-intro body-copy">You have a lifetime of accomplishments. Learning about them is my extraordinary honor. When I meet clients to make a plan for their final years of work and savings, I understand my solemn privilege. Your capital is irreplaceable. My job is to maximize its benefit for your health, family, and legacy.</p>

  <div class="pager" style="top:580px;background:var(--navy)"><svg width="12" height="12" viewBox="0 0 12 12"><path d="M8 2 4 6l4 4" fill="none" stroke="#fff" stroke-width="2"/></svg></div>
  <div class="pager" style="top:620px;border:2px solid var(--navy)"><svg width="12" height="12" viewBox="0 0 12 12"><path d="M4 2l4 4-4 4" fill="none" stroke="#14185c" stroke-width="2"/></svg></div>

  <svg width="0" height="0" style="position:absolute"><defs><path id="star" d="M8 1l2.2 4.6 5 .6-3.7 3.4 1 5L8 12.2 3.5 14.6l1-5L.8 6.2l5-.6z"/></defs></svg>

  <article class="t-card" style="left:112px">
    <h3 class="t-name">ROBIN HALE</h3>
    <div class="stars"><svg width="90" height="16" viewBox="0 0 90 16" fill="#f2b01e"><use href="#star"/><use href="#star" x="18"/><use href="#star" x="36"/><use href="#star" x="54"/><use href="#star" x="72"/></svg></div>
    <p class="body-copy">Lorem ipsum dolor sit amet, consectetur adipiscing elit, sed do eiusmod tempor incididunt ut labore et dolore magna aliqua. Quis ipsum suspendisse ultrices gravida. Risus commodo viverra maecenas accumsan lacus vel facilisis.</p>
  </article>
  <div class="avatar" role="img" aria-label="Client portrait" style="left:262px;top:712px"></div>

  <article class="t-card feature" style="left:492px">
    <h3 class="t-name">STEVEN MARLOW</h3>
    <div class="stars"><svg width="90" height="16" viewBox="0 0 90 16" fill="#f2b01e"><use href="#star"/><use href="#star" x="18"/><use href="#star" x="36"/><use href="#star" x="54"/><use href="#star" x="72"/></svg></div>
    <p class="body-copy">Lorem ipsum dolor sit amet, consectetur adipiscing elit, sed do eiusmod tempor incididunt ut labore et dolore magna aliqua. Quis ipsum suspendisse ultrices gravida. Risus commodo viverra maecenas accumsan lacus vel facilisis.</p>
  </article>
  <div class="avatar" role="img" aria-label="Client portrait" style="left:642px;top:712px"></div>

  <article class="t-card" style="left:880px;width:320px">
    <h3 class="t-name">WALLACE</h3>
    <div class="stars"><svg width="90" height="16" viewBox="0 0 90 16" fill="#f2b01e"><use href="#star"/><use href="#star" x="18"/><use href="#star" x="36"/><use href="#star" x="54"/><use href="#star" x="72"/></svg></div>
    <p class="body-copy">Lorem ipsum dolor sit amet, consectetur adipiscing elit, sed do eiusmod tempor incididunt ut labore et dolore magna aliqua. Quis ipsum suspendisse ultrices gravida. Risus commodo viverra maecenas accumsan lacus vel facilisis.</p>
  </article>
  <div class="avatar" role="img" aria-label="Client portrait" style="left:1020px;top:712px"></div>
</section>

<section class="contact">
  <div class="contact-head">
    <div class="eyebrow">Get in touch</div>
    <h2 class="section-title">CONTACT US</h2>
    <span class="title-rule"></span>
  </div>
  <div class="field" style="left:112px;top:164px;width:224px">First Name</div>
  <div class="field" style="left:346px;top:164px;width:224px">Last Name</div>
  <div class="field" style="left:112px;top:222px;width:224px">Email</div>
  <div class="field" style="left:346px;top:222px;width:224px">Phone</div>
  <div class="field message" style="left:112px;top:280px;width:458px">Message</div>
  <span class="btn">SUBMIT NOW</span>
  <div class="contact-ring"></div>
  <div class="contact-photo" role="img" aria-label="Photo of a happy retired couple relaxing together"></div>
</section>

<footer class="site-footer">
  <div class="f-brand">DORIAN WHITCOMBE</div>
  <p class="f-about">Lorem ipsum dolor sit amet, consectetur adipiscing elit, sed do eiusmod tempor incididunt ut labore et dolore magna aliqua. Quis ipsum suspendisse ultrices gravida. Risus commodo viverra maecenas accumsan lacus vel facilisis.</p>

  <div class="f-col" style="left:540px">
    <h4>QUICK LINKS</h4>
    <ul class="f-links"><li>Home</li><li>About Us</li><li>Specialties</li><li>Testimonials</li><li>Contact Us</li></ul>
  </div>

  <div class="f-col" style="left:716px;width:240px">
    <h4>CONTACT US</h4>
    <div class="contact-row"><span class="c-icon"><svg width="16" height="16" viewBox="0 0 16 16" fill="#14185c"><path d="M3 1h3l1.5 4-2 1.2a9 9 0 0 0 4.3 4.3L11 8.5l4 1.5v3a2 2 0 0 1-2 2A12 12 0 0 1 1 3a2 2 0 0 1 2-2z"/></svg></span><div><b>Phone No:</b><br>(555) 010-0144</div></div>
    <div class="contact-row"><span class="c-icon"><svg width="16" height="16" viewBox="0 0 16 16" fill="none" stroke="#14185c" stroke-width="1.8"><rect x="1.5" y="3.5" width="13" height="9" rx="1"/><path d="M2 4l6 5 6-5"/></svg></span><div><b>Email:</b><br>hello@whitcombeplans.example</div></div>
    <div class="contact-row"><span class="c-icon"><svg width="16" height="16" viewBox="0 0 16 16" fill="#14185c"><path d="M8 1a5 5 0 0 0-5 5c0 4 5 9 5 9s5-5 5-9a5 5 0 0 0-5-5zm0 7a2 2 0 1 1 0-4 2 2 0 0 1 0 4z"/></svg></span><div><b>Location:</b><br>Lorem ipsum dolor sit<br>amet, USA</div></div>
  </div>

  <div class="f-col" style="left:980px">
    <h4>FOLLOW US</h4>
    <div style="margin-top:20px;width:34px;height:34px;border-radius:50%;background:var(--white)"></div>
  </div>

  <div class="copyright">Copyright © 2024 Dorian Whitcombe | All Rights Reserved</div>
</footer>

</body>
</html>
```